Professional Home Buyer business card needed

I need a pretty straight forward business card designed. We help people that NEED to sell their homes solve problems. We perform all types of Real Estate transactions including flip, wholesale, investment, rental property and multi family. The card will mainly be used to give to prospective Sellers but will also be given to Real Estate Investors as well. It should professional and very easy to read, most clients are older people.

Target Market(s)

Distressed home sellers as well as Real Estate investors

Industry/Entity Type

Real Estate

Contact Information for Business Card

should be a professional layout

Colors
ec1f27
ffffff
000000

Requirements
Must have
• Large logo on back and smaller one on front. should utilize Red, white, and black.
• I am thinking of using a soft touch coating on the card so keep that in mind.
• Contact info should be very easy to read, think older clients.
Nice to have
• I would like to see a design with rounded corners on the card
Should not have
• pictures of homes or other home graphics.

```html
<!DOCTYPE html>
<html lang="en">
<head>
<meta charset="utf-8">
<title>Keystone Home Buyers – Business Card</title>
<link rel="stylesheet" href="https://fonts.googleapis.com/css2?family=Lato:wght@400;700;900&display=swap">
<style>
  :root {
    --brand-red: #ec1f27;
    --brand-black: #000000;
    --card-dark: #2a2a2a;
    --brand-white: #ffffff;
    --stage: #d9d9d9;
    --ink: #1c1c1c;
    --faint: #f1f1f1;
  }
  * { box-sizing: border-box; margin: 0; padding: 0; }
  html, body { width: 1200px; height: 900px; overflow: hidden; }
  body {
    background: var(--stage);
    font-family: "Lato", Arial, sans-serif;
    position: relative;
  }
  .card {
    position: absolute;
    width: 540px;
    height: 310px;
    border-radius: 26px;
    overflow: hidden;
    box-shadow: 0 6px 18px rgba(0,0,0,0.18);
  }
  /* Back side */
  .card-back {
    left: 70px; top: 120px;
    background: var(--card-dark);
    display: flex; align-items: center; justify-content: center;
  }
  .wordmark { display: flex; flex-direction: column; align-items: center; }
  .tagline {
    font-weight: 700; font-size: 11px; letter-spacing: 5px;
    color: var(--brand-white); margin-bottom: 8px;
  }
  .wordmark-row { display: flex; align-items: center; gap: 12px; }
  .wordmark-mark { width: 18px; height: 18px; background: var(--brand-red); }
  .wordmark-name {
    font-weight: 900; color: var(--brand-white); text-align: center; line-height: 1;
  }
  .wordmark-name .primary { display: block; font-size: 54px; letter-spacing: 1px; }
  .wordmark-name .secondary { display: block; font-size: 20px; letter-spacing: 7px; margin-top: 8px; }

  /* Front side */
  .card-front {
    left: 590px; top: 460px;
    background: var(--brand-white);
  }
  .faint-field {
    position: absolute; right: 0; top: 0; width: 250px; height: 190px;
    background: linear-gradient(135deg, var(--faint), #f8f8f8);
  }
  .front-logo { position: absolute; left: 30px; top: 32px; align-items: flex-start; }
  .front-logo .tagline { color: var(--ink); font-size: 8px; letter-spacing: 4px; margin-bottom: 5px; }
  .front-logo .wordmark-name { color: var(--brand-black); text-align: left; }
  .front-logo .wordmark-name .primary { font-size: 38px; }
  .front-logo .wordmark-name .secondary { font-size: 14px; letter-spacing: 5px; margin-top: 6px; }
  .front-logo .wordmark-mark { width: 14px; height: 14px; }

  .address {
    position: absolute; right: 30px; top: 38px; text-align: right;
    font-size: 17px; font-style: normal; color: var(--ink); line-height: 1.25;
  }
  .person { position: absolute; left: 30px; top: 150px; }
  .person-name { font-weight: 900; font-size: 24px; color: var(--brand-red); letter-spacing: 0.5px; line-height: 1; }
  .person-title { font-size: 18px; color: var(--ink); margin-top: 2px; }
  .contact-list { list-style: none; margin-top: 8px; }
  .contact-list li {
    display: flex; align-items: center; gap: 8px;
    font-size: 18px; color: var(--ink); line-height: 1.3;
  }
  .contact-list svg { width: 16px; height: 16px; flex: none; }
</style>
</head>
<body>

<section class="card card-back" aria-label="Card back">
  <div class="wordmark">
    <span class="tagline">YOUR FRESH START BEGINS!</span>
    <div class="wordmark-row">
      <span class="wordmark-mark" aria-hidden="true"></span>
      <span class="wordmark-name">
        <span class="primary">KEYSTONE</span>
        <span class="secondary">HOME BUYERS</span>
      </span>
    </div>
  </div>
</section>

<section class="card card-front" aria-label="Card front">
  <div class="faint-field" role="img" aria-label="Faint background decoration of the brand symbol"></div>

  <div class="wordmark front-logo">
    <span class="tagline">YOUR FRESH START BEGINS!</span>
    <div class="wordmark-row">
      <span class="wordmark-name">
        <span class="primary">KEYSTONE</span>
        <span class="secondary">HOME BUYERS</span>
      </span>
      <span class="wordmark-mark" aria-hidden="true"></span>
    </div>
  </div>

  <address class="address">P.O. Box 82<br>Millbrook, KS 67000</address>

  <div class="person">
    <p class="person-name">DALE HARMON</p>
    <p class="person-title">President</p>
    <ul class="contact-list">
      <li>
        <svg viewBox="0 0 16 16" aria-hidden="true"><path fill="#ec1f27" d="M2 4c0-1 1-2 2-2h8c1 0 2 1 2 2v1h-3V4H5v1H2zM3 7h10l1 6H2z"/><circle cx="8" cy="10" r="1.6" fill="#fff"/></svg>
        316-555-0148
      </li>
      <li>
        <svg viewBox="0 0 16 16" aria-hidden="true"><rect x="1" y="3" width="14" height="10" rx="1" fill="#ec1f27"/><path d="M1.5 3.5L8 9l6.5-5.5" fill="none" stroke="#fff" stroke-width="1.3"/></svg>
        dale@prairiehomesforcash.com
      </li>
      <li>
        <svg viewBox="0 0 16 16" aria-hidden="true"><circle cx="8" cy="8" r="7" fill="#ec1f27"/><path d="M8 4a2.6 2.6 0 0 0-2.6 2.6C5.4 8.6 8 12 8 12s2.6-3.4 2.6-5.4A2.6 2.6 0 0 0 8 4z" fill="#fff"/></svg>
        www.prairiehomesforcash.com
      </li>
    </ul>
  </div>
</section>

</body>
</html>
```